Website Design for new skincare product launch/rebranding

The Dew Meridian website is currently live and built through Pagevolt.com. While the existing site has served as a strong starting point, I’m now looking to elevate the overall experience with a complete redesign that reflects the growth and vision of the brand. This will be a full visual and functional revamp — not just a refresh — with the goal of creating a more elevated, intuitive, and conversion-focused platform. I’m looking for a designer who can not only reimagine the layout and visuals, but also collaborate on optimizing the user journey and site structure for both storytelling and sales.

Target Market(s)

Age 25- 45 (core), with secondary appeal to 18-55. Primarily women, but gender inclusive. Wellness/Holistic Beauty/Organic Ingredients, Botanical.

Industry/Entity Type

Beauty, aesthetics, wellness.

Number of Pages Required

5+ page

Font styles to use
Other font styles liked:
• Gravesned Sans Family

Colors

Designer to choose colors to be used in the design.

Requirements
Must have
• Include standard pages (Home, Our Story/Values, Shop, Product Detail with ingredients/description/etc., Contact) and any other recommended sections to optimize conversion. Minimal, clean, calming visual. Seamlessly integrate with Cartwell for all product sales.
Nice to have
• Company colors are attached in images, along with first two products that are launching. One called Velunmist, and one called Petravelle. Fonts and shapes need to align accordingly. Feel elevated, neutral, and luxe while maintaining a grounded, earthy minimalism. Visual inspiration includes brands like Lantern Grove, Marble Osprey, and TOvelin — minimal yet high-end, with thoughtful use of whitespace, typography, and subtle movement. Would LOVE to have movement (short clip GIF) on either the home page or ingredient page, reference TOvelin website (homepage or LuminWeave System™ Tab)
Should not have
• dark colors, complex design elements, too many different fonts. For ingredients, stick to botanical images and information only, with no mentions of CBD or use of leaf imagery.

```html
<!DOCTYPE html>
<html lang="en">
<head>
<meta charset="utf-8">
<title>Dew Meridian — Botanical Balance Meets Science</title>
<link rel="stylesheet" href="https://fonts.googleapis.com/css2?family=Marcellus&family=Montserrat:wght@400;500;600;700&display=swap">
<style>
:root{
  --backdrop:#4d4d4d;
  --hero:#d0d1cf;
  --hero-light:#dcdddb;
  --stone:#9f9f9b;
  --stone-dark:#8f8f8b;
  --ink:#3f3f3d;
  --white:#ffffff;
  --card:#f7f7f7;
  --tile-a:#abacaa;
  --tile-b:#e5e5e3;
  --tile-c:#c6c7c5;
  --tile-d:#dedfdd;
  --blush:#dcd3d2;
  --footer:#9e9e9a;
}
*{box-sizing:border-box;margin:0;padding:0}
html,body{width:1200px;height:2636px;overflow:hidden}
body{background:var(--backdrop);font-family:"Montserrat",sans-serif;color:var(--ink)}
.page{position:absolute;left:81px;top:81px;width:1038px;height:2474px;background:var(--white);overflow:hidden;box-shadow:0 10px 30px rgba(0,0,0,.45)}
.abs{position:absolute}

/* hero */
.hero{position:absolute;left:0;top:0;width:1038px;height:555px;background:var(--hero)}
.wordmark{left:46px;top:22px;font-family:"Marcellus",serif;font-size:44px;letter-spacing:1px;color:var(--stone);line-height:1}
.topline{top:7px;font-size:8px;color:var(--white);display:flex;align-items:center;gap:5px}
.topline b{font-weight:600}
.nav{left:535px;top:27px;width:503px;height:36px;background:var(--stone);clip-path:polygon(28px 0,100% 0,100% 100%,0 100%);display:flex;align-items:center;font-size:9px;letter-spacing:.6px;color:var(--white);font-weight:500}
.nav span{position:absolute}
.nav .contact{border:1px solid var(--white);padding:4px 10px}
.eyebrow{left:46px;top:178px;font-family:"Marcellus",serif;font-size:22px;color:var(--white);letter-spacing:1px}
.headline{left:46px;top:207px;font-family:"Marcellus",serif;font-weight:400;font-size:50px;line-height:52px;color:var(--stone);letter-spacing:1.5px}
.hero-copy{left:46px;top:330px;width:420px;font-size:14.5px;line-height:21px;color:var(--ink)}
.btn{position:absolute;display:flex;align-items:center;justify-content:center;font-family:"Montserrat",sans-serif;font-weight:600;font-size:13px;letter-spacing:.4px}
.btn-solid{background:var(--stone);color:var(--hero-light)}
.btn-outline{border:1.5px solid var(--stone);color:var(--stone)}
.hero-product{left:600px;top:122px;width:270px;height:356px;background:linear-gradient(100deg,#f4f4f4 0%,#e6e6e6 48%,#bdbdbb 52%,#a9a9a7 100%);border-radius:14px}

/* launches */
.section-title{left:0;width:1038px;text-align:center;font-family:"Marcellus",serif;font-weight:400;font-size:35px;color:var(--stone-dark);letter-spacing:1px}
.section-sub{left:0;width:1038px;text-align:center;font-size:14px;color:var(--ink)}
.card{top:703px;width:328px;height:502px;background:var(--card)}
.card-image{position:absolute;left:0;top:0;width:328px;height:300px;background:linear-gradient(180deg,#f1f1f1,#e9e9e9)}
.card-name{position:absolute;top:322px;width:100%;text-align:center;font-family:"Marcellus",serif;font-weight:400;font-size:29px;line-height:34px;color:var(--stone-dark)}
.card-desc{position:absolute;top:369px;left:20px;width:288px;text-align:center;font-size:14px;line-height:21.5px}
.card .btn{top:445px;left:104px;width:120px;height:30px}

/* philosophy */
.tiles{left:46px;top:1342px;width:945px;height:190px;display:flex}
.tile{flex:1;text-align:center;padding-top:22px;overflow:hidden}
.tile:nth-child(1){background:var(--tile-a);color:var(--white)}
.tile:nth-child(2){background:var(--tile-b);color:var(--stone-dark)}
.tile:nth-child(3){background:var(--tile-c);color:var(--white)}
.tile:nth-child(4){background:var(--tile-d);color:var(--stone-dark)}
.tile-icon{width:60px;height:60px;border-radius:50%;margin:0 auto;border:1px solid currentColor;display:flex;align-items:center;justify-content:center}
.tile-icon i{width:22px;height:22px;border-radius:50%;border:1px solid currentColor}
.tile h3{font-family:"Marcellus",serif;font-weight:400;font-size:21px;line-height:24px;margin-top:12px}
.tile p{font-size:10.2px;line-height:14.5px;color:var(--ink);margin:8px auto 0;width:206px}

/* story */
.story-photo{left:165px;top:1593px;width:345px;height:230px;background:linear-gradient(90deg,#d9d9d7 0%,#c9c9c7 49%,#b5aba8 51%,#8e8682 100%)}
.story-eyebrow{left:544px;top:1616px;font-family:"Marcellus",serif;font-size:15px;color:var(--tile-c);letter-spacing:.5px}
.story-title{left:543px;top:1634px;font-family:"Marcellus",serif;font-weight:400;font-size:35px;color:var(--stone-dark);letter-spacing:1px}
.story-copy{left:544px;top:1674px;width:345px;font-size:10.2px;line-height:16px}

/* newsletter */
.newsletter{left:0;top:1883px;width:1038px;height:379px;background:var(--blush)}
.nl-title{top:46px;left:0;width:100%;text-align:center;font-family:"Marcellus",serif;font-weight:400;font-size:35px;color:var(--white);letter-spacing:1px}
.nl-sub{top:92px;left:0;width:100%;text-align:center;font-size:10.5px;line-height:16px}
.field{left:329px;width:390px;background:var(--white);border:1px solid #c9c9c7;font-size:10px;color:#a9a9a7;padding:0 12px}
.subscribe{left:329px;top:299px;width:390px;height:34px;background:var(--stone);color:var(--white);font-size:10px;letter-spacing:1.5px;font-weight:700}

/* footer */
.footer{left:0;top:2262px;width:1038px;height:212px;background:var(--footer);color:var(--white)}
.footer-brand{left:134px;top:54px;width:282px;height:79px;display:flex;align-items:center;gap:14px}
.footer-name{font-family:"Marcellus",serif;font-size:22px;line-height:24px;width:96px}
.footer-tag{background:var(--tile-c);color:var(--ink);font-size:10.5px;line-height:13px;text-align:center;padding:14px 10px;width:170px}
.fcol{top:62px;font-size:10.8px;line-height:16px}
.fcol h4{font-family:"Marcellus",serif;font-weight:400;font-size:14px;letter-spacing:.5px;margin-bottom:2px}
.fcol .row{display:flex;align-items:center;gap:5px}
.dot{width:8px;height:8px;border:1px solid var(--white);border-radius:50%}
.copyright{left:485px;top:176px;font-size:10px}
</style>
</head>
<body>
<div class="page">

  <header class="hero">
    <div class="abs wordmark">DEW MERIDIAN</div>
    <div class="abs topline" style="left:738px">
      <svg width="11" height="8" viewBox="0 0 11 8"><rect x=".5" y=".5" width="10" height="7" fill="none" stroke="#fff"/><path d="M.5 .5 5.5 4.5 10.5 .5" fill="none" stroke="#fff"/></svg>
      Email: <b>hello@dewmeridian.com</b>
    </div>
    <div class="abs topline" style="left:920px">
      <svg width="9" height="9" viewBox="0 0 10 10"><path d="M2 1 4 3 3 4.3C3.7 5.8 4.6 6.6 5.8 7.2L7 6 9 8 7.8 9.3C4.5 8.8 1.3 5.6.8 2.2Z" fill="#fff"/></svg>
      <b>Phone: (555) 014-2290</b>
    </div>
    <nav class="abs nav">
      <span style="left:63px">HOME</span>
      <span style="left:131px">ABOUT</span>
      <span style="left:206px">WHY CHOOSE US</span>
      <span style="left:332px">SERVICES</span>
      <span class="contact" style="left:419px">CONTACT</span>
    </nav>
    <div class="abs eyebrow">BOTANICAL</div>
    <h1 class="abs headline">BALANCE MEETS<br>SCIENCE</h1>
    <p class="abs hero-copy">Discover Velunmist Serum &amp; Petravelle Balm — our newest botanically-infused skincare launches designed to hydrate, nourish and align your skin.</p>
    <a class="btn btn-solid" style="left:46px;top:418px;width:121px;height:31px">SHOP NOW</a>
    <a class="btn btn-outline" style="left:173px;top:418px;width:122px;height:31px">LEARN MORE</a>
    <div class="abs hero-product" role="img" aria-label="Petravelle balm tube beside a Velunmist serum dropper bottle"></div>
  </header>

  <h2 class="abs section-title" style="top:611px">NEW LAUNCHES</h2>
  <p class="abs section-sub" style="top:658px">Elevate your routine with our carefully formulated botanical essentials.</p>

  <article class="abs card" style="left:165px">
    <div class="card-image" role="img" aria-label="Petravelle botanical balm tube"></div>
    <h3 class="card-name">Petravelle Balm</h3>
    <p class="card-desc">A botanical balm that locks in moisture, reduces inflammation, and restores harmony to dry, sensitive skin.</p>
    <a class="btn btn-solid">SHOP BALM</a>
  </article>
  <article class="abs card" style="left:545px">
    <div class="card-image" role="img" aria-label="Velunmist botanical serum dropper bottle"></div>
    <h3 class="card-name">Velunmist Serum</h3>
    <p class="card-desc">A weightless, glass-like serum infused with hydrating botanicals and natural humectants for plump, radiant skin.</p>
    <a class="btn btn-solid">SHOP BALM</a>
  </article>

  <h2 class="abs section-title" style="top:1262px">OUR PHILOSOPHY</h2>
  <p class="abs section-sub" style="top:1309px">Rooted in botanicals, guided by science. Every formula honors your skin and the planet.</p>

  <section class="abs tiles">
    <div class="tile"><div class="tile-icon"><i></i></div><h3>Clean &amp; Organic</h3><p>A botanical balm that locks in moisture, reduces inflammation, and restores harmony to dry, sensitive skin.</p></div>
    <div class="tile"><div class="tile-icon"><i></i></div><h3>Holistic Beauty</h3><p style="width:150px">We treat skin as a whole — mind, body, and spirit — for lasting glow.</p></div>
    <div class="tile"><div class="tile-icon"><i></i></div><h3>Sustainable</h3><p style="width:196px">Eco-friendly packaging and low-impact sourcing guide our every decision.</p></div>
    <div class="tile"><div class="tile-icon"><i></i></div><h3>Botanical Science</h3><p style="width:180px">We pair time-honored botanicals with clinically studied ingredients.</p></div>
  </section>

  <div class="abs story-photo" role="img" aria-label="Serum and balm on marble beside hands applying balm"></div>
  <div class="abs story-eyebrow">DEW MERIDIAN:</div>
  <h2 class="abs story-title">OUR STORY</h2>
  <p class="abs story-copy">Founded with a passion for aligning skin with nature, we create botanically powered skincare that renews, restores and respects your skin's natural harmony. Each product begins with a carefully sourced blend of herbs, flowers and oils, supported by gentle science to deliver visible results without compromise.</p>
  <a class="btn btn-outline" style="left:544px;top:1773px;width:158px;height:30px;font-size:12.5px;border-color:var(--tile-c)">Explore Our Values</a>

  <section class="abs newsletter">
    <h2 class="abs nl-title">STAY ALIGNED</h2>
    <p class="abs nl-sub">Join our newsletter for early access to launches, botanical<br>insights and exclusive offers.</p>
    <div class="abs field" style="top:138px;height:34px;line-height:32px">Your email address</div>
    <div class="abs field" style="top:183px;height:104px;padding-top:10px">Questions or feedback?</div>
    <a class="btn subscribe">SUBSCRIBE</a>
  </section>

  <footer class="abs footer">
    <div class="abs footer-brand">
      <div class="footer-name">Dew Meridian</div>
      <div class="footer-tag">Botanically balanced skincare, crafted for harmony between nature and science.</div>
    </div>
    <div class="abs fcol" style="left:485px"><h4>LINKS</h4><div>▸ Home</div><div>▸ Our Story</div><div>▸ Shop</div><div>▸ Values</div></div>
    <div class="abs fcol" style="left:602px"><h4>Support</h4><div>▸ FAQ</div><div>▸ Shipping &amp; Returns</div><div>▸ Privacy Policy</div><div>▸ Terms of Service</div></div>
    <div class="abs fcol" style="left:769px"><h4>CONTACT</h4>
      <div class="row"><svg width="9" height="7" viewBox="0 0 11 8"><rect x=".5" y=".5" width="10" height="7" fill="#fff"/><path d="M.5 .5 5.5 4.5 10.5 .5" fill="none" stroke="#9e9e9a"/></svg>hello@dewmeridian.com</div>
      <div class="row"><span class="dot"></span>Photoloop</div>
      <div class="row"><span class="dot"></span>ClipWave</div>
    </div>
    <div class="abs copyright">© 2025 Dew Meridian. All rights reserved.</div>
  </footer>

</div>
</body>
</html>
```